upmarket hotel in the mountains needs classy looking menu template

The Larchmere Hotel based in Bright needs two menu templates created ,

restaurant menu... layout is A3 folded in half that will have text on all 4 pa...

Industry/Entity Type

Hospitality

Requirements
Must have
• A combination of any of the logos provided, social media plugs

```html
<!DOCTYPE html>
<html lang="en">
<head>
<meta charset="utf-8">
<title>The Larchmere Hotel – Restaurant Menu Inside Spread</title>
<link rel="stylesheet" href="https://fonts.googleapis.com/css2?family=Cormorant+Garamond:ital,wght@0,600;0,700;1,600;1,700&family=PT+Sans:wght@400;700&display=swap">
<style>
  :root {
    --backdrop: #f3e3c6;
    --paper: #ebe8e2;
    --paper-shade: #dedad2;
    --header-black: #231f1c;
    --accent-orange: #c97a2e;
    --accent-red: #b71c2c;
    --ink: #1c1a18;
    --ink-soft: #4a4540;
    --white: #f4f4f4;
  }
  * { margin: 0; padding: 0; box-sizing: border-box; }
  html, body {
    width: 1200px; height: 819px; overflow: hidden;
    background: var(--backdrop);
  }
  .spread {
    position: absolute; left: 77px; top: 40px;
    width: 1046px; height: 740px;
    display: flex;
    box-shadow: 0 12px 30px rgba(80, 55, 20, 0.25);
  }
  .page { position: relative; width: 523px; height: 740px; overflow: hidden; }
  .page-paper {
    position: absolute; inset: 0;
    background: linear-gradient(160deg, var(--paper) 0%, var(--paper-shade) 100%);
  }
  .page--left .page-paper { box-shadow: inset -10px 0 18px -10px rgba(0,0,0,0.18); }
  .page--right .page-paper { box-shadow: inset 10px 0 18px -10px rgba(0,0,0,0.18); }
  .page-art { position: absolute; inset: 0; }

  .section-band {
    position: absolute; left: 0; right: 0; height: 36px;
    background: var(--accent-orange);
    display: flex; align-items: center; justify-content: center;
    font-family: "Cormorant Garamond", Georgia, serif;
    font-weight: 700; font-size: 21px; letter-spacing: 3px;
    text-transform: uppercase; color: var(--white);
  }
  .section-band--tucked { justify-content: flex-end; padding-right: 34px; }

  .menu-list {
    position: absolute; left: 40px; right: 40px;
    list-style: none;
    font-family: "PT Sans", Arial, sans-serif;
  }
  .menu-item { display: grid; grid-template-columns: 1fr auto; column-gap: 16px; margin-bottom: 10px; }
  .menu-item__name { font-weight: 700; font-size: 14px; color: var(--ink); }
  .menu-item__name .code { color: var(--accent-red); font-size: 12px; margin-left: 4px; }
  .menu-item__price { font-weight: 700; font-size: 14px; color: var(--accent-orange); }
  .menu-item__desc {
    grid-column: 1 / -1; font-size: 12px; line-height: 1.3; color: var(--ink-soft);
  }

  .brand-mark {
    position: absolute; left: 158px; top: 56px; width: 184px;
    text-align: center;
    font-family: "Cormorant Garamond", Georgia, serif;
    font-weight: 700; font-size: 22px; line-height: 1.05; color: var(--header-black);
  }

  .feature-band {
    position: absolute; left: 0; right: 0; top: 420px; height: 110px;
    background: var(--accent-red);
    display: flex; flex-direction: column; align-items: center; justify-content: center;
    color: var(--white); text-align: center;
  }
  .feature-band__title {
    font-family: "Cormorant Garamond", Georgia, serif;
    font-weight: 700; font-size: 24px; letter-spacing: 3px; text-transform: uppercase;
  }
  .feature-band__text {
    font-family: "PT Sans", Arial, sans-serif; font-size: 13px; margin-top: 6px; max-width: 400px; line-height: 1.35;
  }

  .footer-note {
    position: absolute; left: 0; right: 0; bottom: 0; height: 38px;
    background: var(--accent-red);
    display: flex; align-items: center; justify-content: center;
    font-family: "Cormorant Garamond", Georgia, serif;
    font-style: italic; font-weight: 700;
    font-size: 12px; letter-spacing: 0.6px;
    color: var(--white); text-transform: uppercase;
  }
  .dietary-key {
    position: absolute; left: 0; right: 0; top: 556px;
    text-align: center;
    font-family: "PT Sans", Arial, sans-serif; font-weight: 700;
    font-size: 17px; line-height: 1.2; color: var(--ink);
  }
  .dietary-key .code { color: var(--accent-red); }
  .social-plug {
    position: absolute; left: 0; right: 0; bottom: 38px;
    text-align: center;
    font-family: "PT Sans", Arial, sans-serif; font-size: 13px; color: var(--ink-soft);
  }
  .social-plug strong { color: var(--accent-orange); }
</style>
</head>
<body>
  <main class="spread">
    <section class="page page--left">
      <div class="page-paper"></div>
      <div class="section-band section-band--tucked" style="top:48px">Entrées</div>

      <ul class="menu-list" style="top:104px">
        <li class="menu-item"><span class="menu-item__name">Garlic &amp; Herb Flatbread<span class="code">V</span></span><span class="menu-item__price">$12</span><span class="menu-item__desc">Wood-fired dough, roasted garlic butter, sea salt</span></li>
        <li class="menu-item"><span class="menu-item__name">Alpine Trout Rillettes<span class="code">GF</span></span><span class="menu-item__price">$18</span><span class="menu-item__desc">Smoked river trout, pickled shallot, rye crisps</span></li>
        <li class="menu-item"><span class="menu-item__name">Salt &amp; Pepper Calamari<span class="code">S</span></span><span class="menu-item__price">$19</span><span class="menu-item__desc">Chilli, lime aioli, shaved fennel salad</span></li>
      </ul>

      <div class="section-band" style="top:252px">Mains</div>
      <ul class="menu-list" style="top:304px">
        <li class="menu-item"><span class="menu-item__name">Slow-Braised Lamb Shoulder<span class="code">GF</span></span><span class="menu-item__price">$38</span><span class="menu-item__desc">Rosemary jus, crushed potatoes, seasonal greens</span></li>
        <li class="menu-item"><span class="menu-item__name">Wild Mushroom Risotto<span class="code">V</span></span><span class="menu-item__price">$30</span><span class="menu-item__desc">Porcini, truffle oil, aged parmesan, chives</span></li>
      </ul>

      <div class="section-band" style="top:422px">Desserts</div>
      <ul class="menu-list" style="top:478px">
        <li class="menu-item"><span class="menu-item__name">Dark Chocolate Fondant<span class="code">N</span></span><span class="menu-item__price">$16</span><span class="menu-item__desc">Hazelnut praline, vanilla bean ice cream</span></li>
        <li class="menu-item"><span class="menu-item__name">Poached Pear Tart</span><span class="menu-item__price">$15</span><span class="menu-item__desc">Spiced red wine, almond cream, crème fraîche</span></li>
        <li class="menu-item"><span class="menu-item__name">Coconut Panna Cotta<span class="code">VE</span></span><span class="menu-item__price">$14</span><span class="menu-item__desc">Passionfruit, toasted coconut, mint</span></li>
        <li class="menu-item"><span class="menu-item__name">Local Cheese Board</span><span class="menu-item__price">$24</span><span class="menu-item__desc">Three regional cheeses, quince paste, lavosh</span></li>
      </ul>

      <svg class="page-art" viewBox="0 0 523 740" aria-hidden="true">
        <path d="M0 0 H523 V30 Q230 18 0 110 Z" fill="var(--header-black)"/>
        <path d="M0 110 Q230 18 523 30" fill="none" stroke="var(--accent-orange)" stroke-width="3"/>
      </svg>
      <p class="footer-note">Full range of pizzas available in the bistro and bar. Gluten free available.</p>
    </section>

    <section class="page page--right">
      <div class="page-paper"></div>
      <svg class="page-art" viewBox="0 0 523 740" aria-hidden="true">
        <circle cx="250" cy="40" r="92" fill="var(--white)" stroke="var(--accent-orange)" stroke-width="4"/>
        <path d="M0 0 H523 V48 Q250 -30 0 82 Z" fill="var(--header-black)"/>
        <path d="M0 82 Q250 -30 523 48" fill="none" stroke="var(--accent-orange)" stroke-width="3"/>
      </svg>
      <p class="brand-mark">The Larchmere<br>Hotel</p>

      <div class="section-band" style="top:176px">Sides</div>
      <ul class="menu-list" style="top:230px">
        <li class="menu-item"><span class="menu-item__name">Rosemary Fries<span class="code">VE</span></span><span class="menu-item__price">$9</span><span class="menu-item__desc">Sea salt, garlic aioli</span></li>
        <li class="menu-item"><span class="menu-item__name">Roasted Heirloom Carrots<span class="code">GF</span></span><span class="menu-item__price">$11</span><span class="menu-item__desc">Honey glaze, dukkah, yoghurt</span></li>
        <li class="menu-item"><span class="menu-item__name">Garden Leaf Salad<span class="code">V</span></span><span class="menu-item__price">$10</span><span class="menu-item__desc">Mixed leaves, radish, house vinaigrette</span></li>
        <li class="menu-item"><span class="menu-item__name">Buttered Greens<span class="code">GF</span></span><span class="menu-item__price">$10</span><span class="menu-item__desc">Broccolini, beans, toasted almonds</span></li>
      </ul>

      <div class="feature-band">
        <p class="feature-band__title">Chef's Specials</p>
        <p class="feature-band__text">Ask your server about tonight's seasonal dishes, made with produce from the valley.</p>
      </div>

      <p class="dietary-key">
        <span class="code">V</span>- Vego, <span class="code">N</span>- Traces of Nuts<br>
        <span class="code">GF</span>- Gluten Free, <span class="code">S</span>- Spicy <span class="code">VE</span>- Vegan
      </p>
      <p class="social-plug">Share your meal with us on social media &nbsp;<strong>@larchmerehotel</strong></p>
    </section>
  </main>
</body>
</html>
```